Bramblecrest IT Solutions Web Design

We are a new business in Perth Australia specializing in supporting Home residential and Small business with their IT requirements
We believe image and presentation is important and having a eye catching, professional, intuitive website is a must.
Although we are still expanding as business the message we would like to convey to users is that they can trust our work.

Services we provide are
Please refer to text file attached

Future services
- Email hosting
- Domain resller
- Cloud services

A wordpress theme i really like is below.
http://www.layoutquarry.example/wordpress-themes/58316.html
Orange colour included is a preference however a colour that goes withg my logo is fine too.

The logo i would like to include is also attached.

I would like the web site design to be built and coded in wordpress and handed over to me so i can continue updating the content, source will be require.

Target Market(s)

Home residential and Small business users

Industry/Entity Type

Residential

Requirements
Must have
• The form to email function in the contact us page.
Nice to have
• Interactive icons

```html
<!DOCTYPE html>
<html lang="en">
<head>
<meta charset="utf-8">
<title>Bramblecrest IT Solutions</title>
<link href="https://fonts.googleapis.com/css2?family=Open+Sans:ital,wght@0,300;0,400;0,600;0,700;1,400;1,600;1,700&display=swap" rel="stylesheet">
<style>
:root{
  --orange:#d65a0c;
  --orange-band:#e0692c;
  --orange-soft:#f3a477;
  --orange-text:#e2702f;
  --ink:#222;
  --grey:#8b8b8b;
  --rule:#f1c7ae;
  --white:#fff;
  --hero-dark:#1c1c1e;
  --badge:#d3d3d3;
}
*{box-sizing:border-box;margin:0;padding:0}
html,body{width:963px;height:1200px;overflow:hidden;background:var(--white)}
body{font-family:"Open Sans",Arial,sans-serif;color:var(--ink);position:relative}
.abs{position:absolute}
/* header */
.site-header{position:absolute;left:0;top:0;width:963px;height:76px;background:rgba(110,110,112,.92);z-index:2}
.brand{position:absolute;left:78px;top:26px;display:flex;align-items:center;gap:8px}
.brand-mark{width:24px;height:24px;background:var(--ink)}
.brand-name{font-size:20px;font-weight:600;color:var(--orange-text);letter-spacing:.5px}
.main-nav a{position:absolute;top:47px;font-size:11px;color:var(--white);text-decoration:none;text-transform:uppercase}
.main-nav a.active{color:var(--orange-text)}
.nav-underline{position:absolute;left:389px;top:70px;width:67px;height:6px;background:var(--orange-text)}
/* hero */
.hero{position:absolute;left:0;top:0;width:963px;height:471px;
  background:radial-gradient(ellipse at 55% 35%,#5e5a57 0%,#34312f 35%,var(--hero-dark) 75%)}
.hero h1,.hero h2,.hero p{position:absolute;left:0;width:963px;text-align:center;color:var(--white)}
.hero h1{top:198px;font-size:35px;font-weight:700;letter-spacing:.5px}
.hero h2{top:258px;font-size:26px;font-weight:600}
.hero p{top:314px;font-size:21px;font-weight:300}
.hero-rule{position:absolute;left:323px;top:405px;width:317px;height:1px;background:#999}
.pager{position:absolute;top:428px;width:10px;height:10px;border-radius:50%;background:var(--white)}
.pager.on{background:var(--orange-text)}
/* services */
.services{position:absolute;left:0;top:471px;width:963px;height:238px;background:var(--orange)}
.pointer{position:absolute;left:467px;top:471px;width:0;height:0;border-left:15px solid transparent;border-right:15px solid transparent;border-top:19px solid var(--hero-dark)}
.service{position:absolute;top:39px;width:200px;text-align:center}
.service .ring{width:80px;height:80px;margin:0 auto;border:2px solid var(--white);border-radius:50%;padding:3px}
.service .disc{width:100%;height:100%;border-radius:50%;background:var(--white);display:flex;align-items:center;justify-content:center}
.service h3{margin-top:17px;font-size:12.5px;font-weight:600;color:var(--white);letter-spacing:.5px}
.service p{margin-top:8px;font-size:9.6px;line-height:17px;color:var(--orange-soft);letter-spacing:.3px}
/* band */
.promo{position:absolute;left:0;top:709px;width:963px;height:44px;background:var(--orange-band)}
.promo .lead{position:absolute;left:231px;top:13px;font-size:12px;font-weight:700;font-style:italic;color:var(--white)}
.promo .note{position:absolute;left:581px;top:15px;font-size:10px;color:var(--white)}
.promo .line{position:absolute;top:22px;height:1px;background:#f4b08c}
.promo .dot{position:absolute;top:19px;width:6px;height:6px;border-radius:50%;background:#f7c4a6}
/* info */
.toll{position:absolute;left:64px;width:129px;text-align:right}
.toll .label{position:absolute;top:793px;font-size:13px;color:var(--orange-text)}
.rule{position:absolute;height:3px;border-top:1px solid var(--rule);border-bottom:1px solid var(--rule)}
.phone{position:absolute;left:70px;top:813px;font-size:17px;font-weight:400}
.address{position:absolute;left:90px;top:862px;width:103px;text-align:right;font-size:9px;line-height:17.5px}
.email{position:absolute;left:108px;top:948px;font-size:9.5px;color:var(--ink);text-decoration:underline}
.pitch h2{position:absolute;left:255px;top:794px;font-size:17px;font-weight:400;color:var(--orange-text)}
.pitch h3{position:absolute;left:256px;top:822px;font-size:12px;font-weight:400;line-height:21px}
.pitch p.body{position:absolute;left:256px;top:882px;width:164px;font-size:9.6px;line-height:20px;color:var(--grey);white-space:nowrap;overflow:hidden}
.photo{position:absolute;left:430px;top:799px;width:162px;height:160px;background:linear-gradient(160deg,#c9d3dc 0%,#7c8ea3 45%,#2a3a55 100%)}
.quote{position:absolute;left:256px;top:982px;width:360px;font-size:9px;font-style:italic;line-height:20px}
.quote .mark{color:var(--orange-text);font-size:12px}
.quote .by{position:absolute;left:227px;top:20px;color:var(--orange-text);font-style:normal}
.list-col h2{position:absolute;top:794px;font-size:17px;font-weight:400;color:var(--orange-text)}
.list-col ul{position:absolute;top:841px;list-style:none}
.list-col li{position:relative;padding-left:13px;font-size:9.6px;height:20px}
.list-col li::before{content:"";position:absolute;left:0;top:5px;width:4px;height:4px;border-radius:50%;background:var(--orange-text)}
/* footer */
.footer-rule{position:absolute;left:0;top:1046px;width:963px;height:1px;background:#ddd}
.footer-brand{position:absolute;left:64px;top:1074px;display:flex;align-items:center;gap:5px}
.footer-brand .sq{width:10px;height:10px;background:#999}
.footer-brand span{font-size:10px;font-weight:600;color:#999}
.copy{position:absolute;left:64px;top:1093px;font-size:9.5px;color:var(--grey)}
.links{position:absolute;top:1071px;list-style:none}
.links li{height:20px;font-size:9.6px;color:var(--orange-text);padding-left:13px;position:relative}
.links li::before{content:"";position:absolute;left:1px;top:5px;width:4px;height:4px;border-top:1px solid var(--ink);border-right:1px solid var(--ink);transform:rotate(45deg)}
.badge{position:absolute;background:var(--badge)}
</style>
</head>
<body>

<section class="hero" role="img" aria-label="Photo of a businessman holding a glowing light bulb in his open hand">
  <h1>SUPPORTING HOME RESIDENTIAL</h1>
  <h2>AND SMALL BUSINESS WITH THEIR</h2>
  <p>IT REQUIREMENTS</p>
  <div class="hero-rule"></div>
  <span class="pager on" style="left:445px"></span>
  <span class="pager" style="left:466px"></span>
  <span class="pager" style="left:487px"></span>
  <span class="pager" style="left:509px"></span>
</section>

<header class="site-header">
  <div class="brand"><span class="brand-mark"></span><span class="brand-name">Bramblecrest IT Solutions</span></div>
  <nav class="main-nav">
    <a class="active" href="#" style="left:408px">Home</a>
    <a href="#" style="left:514px">About us</a>
    <a href="#" style="left:636px">Services</a>
    <a href="#" style="left:753px">Blog</a>
    <a href="#" style="left:847px">Contacts</a>
  </nav>
  <div class="nav-underline"></div>
</header>

<section class="services">
  <div class="service" style="left:70px">
    <div class="ring"><div class="disc">
      <svg width="34" height="30" viewBox="0 0 34 30"><g fill="none" stroke="#d65a0c" stroke-width="4" stroke-dasharray="3 2.2"><circle cx="12" cy="16" r="8"/><circle cx="26" cy="9" r="5"/><circle cx="26" cy="23" r="4.5"/></g><g fill="#d65a0c"><circle cx="12" cy="16" r="6"/><circle cx="26" cy="9" r="3.5"/><circle cx="26" cy="23" r="3"/></g><g fill="#fff"><circle cx="12" cy="16" r="2.5"/><circle cx="26" cy="9" r="1.4"/><circle cx="26" cy="23" r="1.2"/></g></svg>
    </div></div>
    <h3>TECHNICAL SUPPORT</h3>
    <p>Praesent vestibulum aenean nonummy hendrerit mauris. Hasellus porta. Fusce suscipit varius mi. Cum sociis nato.</p>
  </div>
  <div class="service" style="left:279px">
    <div class="ring"><div class="disc">
      <svg width="28" height="28" viewBox="0 0 28 28"><circle cx="14" cy="14" r="13" fill="#d65a0c"/><path d="M8 7c3 0 5 2 4 4s-4 1-4 4 3 3 2 6c-3-1-6-5-6-8 0-3 2-5 4-6zM17 5c3 1 6 4 6 8-2 0-3-1-4 1s1 4-1 6c-2-2-1-4-3-5s-1-4 1-5-1-3 1-5z" fill="#fff"/></svg>
    </div></div>
    <h3>NETWORK SOLUTIONS</h3>
    <p>Praesent vestibulum aenean nonummy hendrerit mauris. Hasellus porta. Fusce suscipit varius mi. Cum sociis nato.</p>
  </div>
  <div class="service" style="left:487px">
    <div class="ring"><div class="disc">
      <svg width="32" height="26" viewBox="0 0 32 26" fill="#d65a0c"><circle cx="7" cy="7" r="4"/><circle cx="25" cy="7" r="4"/><circle cx="16" cy="9" r="5"/><path d="M1 20c0-5 3-7 6-7s5 1 5 2v5zM31 20c0-5-3-7-6-7s-5 1-5 2v5z"/><path d="M8 26c0-7 4-10 8-10s8 3 8 10z"/></svg>
    </div></div>
    <h3>ONSITE SUPPORT</h3>
    <p>Praesent vestibulum aenean nonummy hendrerit mauris. Hasellus porta. Fusce suscipit varius mi. Cum sociis nato.</p>
  </div>
  <div class="service" style="left:695px">
    <div class="ring"><div class="disc">
      <svg width="32" height="28" viewBox="0 0 32 28"><rect x="1" y="1" width="30" height="20" rx="2" fill="#d65a0c"/><rect x="4" y="4" width="24" height="13" fill="#fff"/><rect x="13" y="21" width="6" height="4" fill="#d65a0c"/><rect x="8" y="25" width="16" height="2" fill="#d65a0c"/></svg>
    </div></div>
    <h3>REMORT SUPPORT</h3>
    <p>Praesent vestibulum aenean nonummy hendrerit mauris. Hasellus porta. Fusce suscipit varius mi. Cum sociis nato.</p>
  </div>
</section>
<div class="pointer"></div>

<section class="promo">
  <span class="dot" style="left:64px"></span><span class="dot" style="left:76px"></span><span class="dot" style="left:88px"></span><span class="dot" style="left:99px"></span><span class="dot" style="left:106px"></span>
  <span class="line" style="left:106px;width:107px"></span>
  <span class="lead">Are you Waiting for getting FREE 24/7 Hosting Solutions ?</span>
  <span class="note">It will be coming soon..........!!!</span>
  <span class="line" style="left:741px;width:107px"></span>
  <span class="dot" style="left:842px"></span><span class="dot" style="left:852px"></span><span class="dot" style="left:863px"></span><span class="dot" style="left:875px"></span><span class="dot" style="left:886px"></span>
</section>

<section class="contact-block">
  <div class="toll"><span class="label" style="right:0">Call us toll free:</span></div>
  <div class="phone">1 800 555 0199</div>
  <div class="rule" style="left:67px;top:844px;width:126px"></div>
  <svg class="abs" style="left:64px;top:862px" width="28" height="32" viewBox="0 0 28 32"><circle cx="14" cy="13" r="12" fill="#a9a9a9" stroke="#a9a9a9" stroke-width="3" stroke-dasharray="3 2"/><path d="M14 6a6 6 0 0 1 6 6c0 5-6 12-6 12s-6-7-6-12a6 6 0 0 1 6-6z" fill="#e2702f"/><circle cx="14" cy="12" r="2.2" fill="#fff"/></svg>
  <div class="address">USA – SPRINGDALE,<br>418 HARLOW STREET,<br>EASTBROOK, CA 90512</div>
  <div class="rule" style="left:67px;top:923px;width:126px"></div>
  <svg class="abs" style="left:67px;top:942px" width="29" height="18" viewBox="0 0 29 18"><rect width="29" height="18" fill="#e2702f"/><path d="M0 0l14.5 11L29 0" fill="none" stroke="#f7c4a6" stroke-width="2"/></svg>
  <a class="email" href="#">mail@bramblecrest.example</a>
</section>

<section class="pitch">
  <h2>Need IT Solutions ?</h2>
  <h3>LEADING MANAGED<br>SERVICE PROVIDER</h3>
  <div class="rule" style="left:255px;top:869px;width:153px"></div>
  <p class="body">Praesent vestibulum aenean nonum<br>hendrerit mauris. Hasellus porta. Fus<br>suscipit varius mi. Cum sociis natoqu<br>penatibus magnis dis parturient.</p>
  <div class="photo" role="img" aria-label="Photo of a smiling businessman in a suit with two colleagues in an office"></div>
  <p class="quote"><span class="mark">“</span> Aenean nonummy hendrerit mau phasellu porta. Fusce suscipit varius mi sed. Cum<br>sociis natoque penatibus et magnis dis... <span class="mark">”</span><span class="by">- Liam Carter( Head Manager )</span></p>
</section>

<section class="list-col">
  <h2 style="left:659px">Featured :</h2>
  <div class="rule" style="left:659px;top:822px;width:83px"></div>
  <ul style="left:659px">
    <li>Managed Services</li><li>Virtual Office</li><li>Strategic Planning</li><li>Installation</li><li>Mobile IT</li><li>Network Security</li>
  </ul>
  <h2 style="left:815px">Popular :</h2>
  <div class="rule" style="left:815px;top:822px;width:83px"></div>
  <ul style="left:815px">
    <li>Email</li><li>Web Hosting</li><li>Offsite Backup</li><li>Internet Access</li><li>VoIP</li><li>Digital Media</li>
  </ul>
</section>

<footer>
  <div class="footer-rule"></div>
  <div class="footer-brand"><span class="sq"></span><span>Bramblecrest IT Solutions</span></div>
  <div class="copy">© 2015 Privacy Policy</div>
  <ul class="links" style="left:226px"><li>About us</li><li>Work team</li><li>What we do</li><li>Clients</li><li>Management</li></ul>
  <ul class="links" style="left:375px"><li>Market research</li><li>Online support</li><li>Financial services</li><li>Business help</li><li>Premises</li></ul>
  <ul class="links" style="left:525px"><li>Strategies</li><li>Recent issues</li><li>FAQ</li><li>Solutions</li><li>Contacts</li></ul>
  <div class="badge" style="left:668px;top:1072px;width:46px;height:24px;border-radius:12px"></div>
  <div class="badge" style="left:739px;top:1076px;width:70px;height:16px;border-radius:3px"></div>
  <div class="badge" style="left:834px;top:1074px;width:64px;height:20px"></div>
  <div class="badge" style="left:668px;top:1124px;width:86px;height:20px;border-radius:10px"></div>
  <div class="badge" style="left:771px;top:1122px;width:102px;height:24px;border-radius:3px"></div>
</footer>

</body>
</html>
```